TRV business card

Need a business card for a company that provides instructional design and elearning development services. The website is here: http://tarvexa.studio/

I'm attaching a current logo, as well as the old business card design. While I like to keep it clean, the old design is too simplistic for my liking. The only idea I want to reuse from the old design is placing industry jargon on the back of the card, just need a better way to present it. But if you have other ideas for the back--feel free to experiment.

Please use the colors complementary to the color we have on the website. Thank you!

```html
<!DOCTYPE html>
<html lang="en">
<head>
<meta charset="utf-8">
<title>TRV business card</title>
<link href="https://fonts.googleapis.com/css2?family=Source+Sans+3:wght@400;600;700&display=swap" rel="stylesheet">
<style>
  :root {
    --backdrop: #3a3330;
    --card: #121212;
    --teal: #2fb8aa;
    --gold: #cdb57c;
    --ink: #f2f2f2;
    --muted: #d9d9d9;
  }
  * { box-sizing: border-box; margin: 0; padding: 0; }
  html, body {
    width: 1200px; height: 814px; overflow: hidden;
    background: var(--backdrop);
    font-family: "Source Sans 3", "Helvetica Neue", Arial, sans-serif;
  }
  .canvas { position: relative; width: 1200px; height: 814px; }
  .card {
    position: absolute; width: 540px; height: 309px;
    background: var(--card); border-radius: 4px;
    box-shadow: 0 10px 28px rgba(0,0,0,.45);
    color: var(--ink);
  }
  .card--front { left: 50px; top: 420px; }
  .card--back { left: 610px; top: 90px; }

  /* brand name lockup */
  .brand { display: flex; align-items: center; gap: 8px; color: var(--teal); font-weight: 700; }
  .brand__dot { width: 14px; height: 14px; background: var(--teal); border-radius: 50%; }
  .card--front .brand { position: absolute; top: 26px; right: 36px; font-size: 22px; }

  .rule { position: absolute; left: 200px; right: 36px; top: 156px; height: 1px; background: var(--gold); }
  .person { position: absolute; left: 36px; top: 132px; }
  .person__name { color: var(--teal); font-size: 26px; font-weight: 700; line-height: 1.1; }
  .person__role { color: var(--gold); font-size: 17px; margin-top: 4px; }

  .contact { position: absolute; left: 36px; bottom: 30px; list-style: none; font-size: 16px; }
  .contact li { display: flex; align-items: center; gap: 10px; margin-top: 7px; }
  .contact svg { width: 16px; height: 16px; fill: var(--teal); flex: none; }

  .website { position: absolute; right: 36px; top: 176px; display: flex; align-items: center; gap: 8px; font-size: 16px; }
  .website svg { width: 16px; height: 16px; }

  /* back */
  .services { position: absolute; left: 34px; top: 30px; list-style: none; font-size: 15px; color: var(--muted); }
  .services li { display: flex; align-items: center; gap: 9px; line-height: 23px; }
  .services li::before { content: ""; width: 5px; height: 5px; border-radius: 50%; background: var(--teal); }
  .services .services__heading { color: var(--teal); font-size: 19px; font-weight: 700; line-height: 28px; }
  .services .services__heading::before { display: none; }
  .card--back .brand { position: absolute; left: 34px; bottom: 30px; font-size: 38px; line-height: 1; }
  .card--back .brand__dot { width: 22px; height: 22px; }
</style>
</head>
<body>
<main class="canvas">
  <section class="card card--front" aria-label="Business card front">
    <div class="brand"><span class="brand__dot"></span>Tarvexa Studio</div>
    <div class="person">
      <h1 class="person__name">Marek Holloway</h1>
      <p class="person__role">CEO/Founder</p>
    </div>
    <div class="rule"></div>
    <div class="website">
      www.tarvexa.studio
      <svg viewBox="0 0 16 16"><circle cx="8" cy="8" r="7" fill="none" stroke="var(--teal)" stroke-width="1.6"/><path d="M1 8h14M8 1c-3 4-3 10 0 14M8 1c3 4 3 10 0 14" fill="none" stroke="var(--teal)" stroke-width="1.2"/></svg>
    </div>
    <ul class="contact">
      <li>
        <svg viewBox="0 0 16 16"><path d="M3.6 1.2l2.3 2.9-1.3 1.8c.9 2 2.6 3.7 4.6 4.6l1.8-1.3 2.9 2.3-1.4 2.4C7.2 13.6 2.4 8.8 1.2 3.1z"/></svg>
        555-014-2738
      </li>
      <li>
        <svg viewBox="0 0 16 16"><path d="M1 3h14v10H1z"/><path d="M1 3l7 6 7-6" fill="none" stroke="var(--card)" stroke-width="1.4"/></svg>
        mholloway@tarvexa.studio
      </li>
    </ul>
  </section>

  <section class="card card--back" aria-label="Business card back">
    <ul class="services">
      <li>Mobile Learning Scorm</li>
      <li>Instructional Design LMS</li>
      <li>Moocs Elearning HTML5</li>
      <li class="services__heading">How can we help?</li>
      <li>Adult Learning Theory</li>
      <li>Gamification Classroom</li>
      <li>XAPI Blended learning</li>
    </ul>
    <div class="brand"><span class="brand__dot"></span>Tarvexa Studio</div>
  </section>
</main>
</body>
</html>
```